Brivora Collective Business Card Design

We need a business card design for Brivora Collective. We are a healthcare recruiting, wellness and education company. We partner with medical facilities to find quality candidates. We also offer free wellness courses.
The final design should communicate an emphasis on recruiting and wellness
The main purpose of the business card is to utilized it for networking events, give to hospitals, executives, VCs surgery centers and clinics. I want it to be sleek, clean, use of our brand colors and professional.

```html
<!DOCTYPE html>
<html lang="en">
<head>
<meta charset="UTF-8">
<title>Brivora Collective – Business Card</title>
<link href="https://fonts.googleapis.com/css2?family=Lato:wght@300;400;700;900&display=swap" rel="stylesheet">
<style>
  :root {
    --teal: #005a52;
    --teal-edge: #004a43;
    --white: #ffffff;
    --soft-white: rgba(255,255,255,0.88);
    --divider: rgba(255,255,255,0.35);
    --backdrop: #2a2b2d;
    --backdrop-light: #3a3b3e;
  }
  * { margin: 0; padding: 0; box-sizing: border-box; }
  html, body {
    width: 1200px; height: 952px; overflow: hidden;
  }
  body {
    background: radial-gradient(ellipse at 55% 50%, var(--backdrop-light), var(--backdrop) 70%);
    font-family: 'Lato', sans-serif;
    position: relative;
  }
  .card {
    position: absolute;
    left: 250px;
    width: 700px;
    height: 400px;
    background: var(--teal);
    box-shadow: 0 14px 30px rgba(0,0,0,0.45);
    overflow: hidden;
    color: var(--white);
  }
  .card--front { top: 56px; }
  .card--back { top: 496px; }

  /* Front */
  .brand-lockup {
    position: absolute;
    left: 50%; top: 50%;
    transform: translate(-50%, -50%);
    display: flex; align-items: center; gap: 18px;
  }
  .brand-lockup__mark {
    width: 30px; height: 30px;
    background: var(--white);
  }
  .brand-lockup__name {
    font-size: 44px; font-weight: 300; letter-spacing: 0.5px;
    white-space: nowrap;
  }

  /* Back */
  .accent-strip {
    position: absolute;
    width: 12px;
    background: var(--white);
  }
  .accent-strip--top { left: 0; top: 0; height: 150px; }
  .accent-strip--bottom { right: 0; bottom: 0; height: 150px; }

  .back-brand {
    position: absolute;
    left: 60px; top: 120px;
    display: flex; align-items: center; gap: 12px;
  }
  .back-brand__mark { width: 18px; height: 18px; background: var(--white); }
  .back-brand__name { font-size: 24px; font-weight: 300; white-space: nowrap; }

  .divider {
    position: absolute;
    left: 350px; top: 95px;
    width: 1px; height: 175px;
    background: var(--divider);
  }

  .contact {
    position: absolute;
    left: 385px; top: 100px;
  }
  .contact__name {
    font-size: 22px; font-weight: 400; letter-spacing: 1px;
    text-transform: uppercase;
  }
  .contact__name strong { font-weight: 900; }
  .contact__role {
    font-size: 14px; font-weight: 300; color: var(--soft-white);
    margin-top: 2px; margin-bottom: 18px;
  }
  .contact__list { list-style: none; }
  .contact__item {
    display: flex; align-items: center; gap: 10px;
    font-size: 14px; font-weight: 400; margin-bottom: 8px;
  }
  .contact__icon { width: 14px; height: 14px; flex: none; }

  .address {
    position: absolute;
    left: 60px; bottom: 60px;
    font-size: 13px; font-weight: 400; color: var(--soft-white);
  }
</style>
</head>
<body>

  <section class="card card--front" aria-label="Card front">
    <div class="brand-lockup">
      <span class="brand-lockup__mark"></span>
      <span class="brand-lockup__name">Brivora Collective</span>
    </div>
  </section>

  <section class="card card--back" aria-label="Card back">
    <span class="accent-strip accent-strip--top"></span>
    <span class="accent-strip accent-strip--bottom"></span>

    <div class="back-brand">
      <span class="back-brand__mark"></span>
      <span class="back-brand__name">Brivora Collective</span>
    </div>

    <span class="divider"></span>

    <div class="contact">
      <p class="contact__name">Daniel R. <strong>Whitcombe</strong></p>
      <p class="contact__role">Managing Director</p>
      <ul class="contact__list">
        <li class="contact__item">
          <svg class="contact__icon" viewBox="0 0 24 24" aria-hidden="true"><path fill="#fff" d="M6.6 10.8a15.1 15.1 0 0 0 6.6 6.6l2.2-2.2c.3-.3.7-.4 1-.2 1.1.4 2.3.6 3.6.6.6 0 1 .4 1 1V20c0 .6-.4 1-1 1A17 17 0 0 1 3 4c0-.6.4-1 1-1h3.5c.6 0 1 .4 1 1 0 1.3.2 2.5.6 3.6.1.3 0 .7-.2 1z"/></svg>
          +00 987 654 32
        </li>
        <li class="contact__item">
          <svg class="contact__icon" viewBox="0 0 24 24" aria-hidden="true"><path fill="#fff" d="M2 5h20v14H2z"/><path fill="none" stroke="#005a52" stroke-width="2" d="M2 5l10 8 10-8"/></svg>
          hello@brivoramail.com
        </li>
        <li class="contact__item">
          <svg class="contact__icon" viewBox="0 0 24 24" aria-hidden="true"><circle cx="12" cy="12" r="10" fill="#fff"/><path fill="none" stroke="#005a52" stroke-width="1.6" d="M2 12h20M12 2c3 3 3 17 0 20M12 2c-3 3-3 17 0 20"/></svg>
          www.brivoracollective.com
        </li>
      </ul>
    </div>

    <p class="address">2174 Linden Park Avenue Arlington, VA 22201</p>
  </section>

</body>
</html>
```